KORVELTA Corporate Business Card

Modern business card design for company which focuses in the areas of Staffing, IT Consulting & Data Services. Please note: We are no longer using the IT subscript on the logo. All designs should have IT subscript removed.
Website: www.korveltait.example

```html
<!DOCTYPE html>
<html lang="en">
<head>
<meta charset="utf-8">
<title>KORVELTA Business Card</title>
<link rel="stylesheet" href="https://fonts.googleapis.com/css2?family=Open+Sans:wght@400;600&display=swap">
<style>
  :root {
    --backdrop: #5f6965;
    --card-white: #eceeed;
    --card-blue: #2b9ad6;
    --brand-blue: #1f8fd0;
    --brand-deep: #1d5f9e;
    --ink: #1d2a3a;
    --emboss: #2286c2;
  }
  html, body {
    margin: 0;
    width: 1200px;
    height: 1200px;
    overflow: hidden;
    background: var(--backdrop);
    font-family: "Open Sans", Arial, sans-serif;
  }
  .sheet {
    width: 1200px;
    height: 1200px;
    display: flex;
    flex-direction: column;
    align-items: center;
    justify-content: center;
    gap: 60px;
  }
  .card {
    position: relative;
    width: 700px;
    height: 400px;
    box-sizing: border-box;
  }
  .card--front {
    background: var(--card-white);
    border-bottom: 6px solid var(--card-blue);
  }
  .card--back {
    background: var(--card-blue);
    display: flex;
    align-items: center;
    justify-content: center;
  }
  .identity {
    position: absolute;
    left: 56px;
    top: 60px;
  }
  .identity__name {
    margin: 0;
    font-size: 30px;
    font-weight: 400;
    color: var(--ink);
  }
  .identity__title {
    margin: 2px 0 0;
    font-size: 18px;
    color: var(--brand-blue);
  }
  .contacts {
    position: absolute;
    left: 56px;
    bottom: 48px;
    margin: 0;
    padding: 0;
    list-style: none;
    font-size: 17px;
    color: var(--ink);
  }
  .contacts__item {
    display: flex;
    align-items: center;
    gap: 12px;
    margin-top: 8px;
  }
  .contacts__icon {
    width: 16px;
    height: 16px;
    fill: var(--brand-blue);
  }
  .brand {
    display: flex;
    align-items: center;
    gap: 12px;
  }
  .brand--front {
    position: absolute;
    right: 48px;
    bottom: 70px;
  }
  .brand__mark {
    width: 22px;
    height: 22px;
    background: var(--brand-blue);
  }
  .brand__name {
    font-weight: 600;
    font-size: 34px;
    letter-spacing: 2px;
    color: var(--brand-deep);
  }
  .brand--back .brand__mark {
    width: 48px;
    height: 48px;
    background: var(--emboss);
  }
  .brand--back .brand__name {
    font-size: 82px;
    letter-spacing: 6px;
    color: var(--emboss);
  }
</style>
</head>
<body>
<main class="sheet">
  <section class="card card--front">
    <div class="identity">
      <h1 class="identity__name">Your Name</h1>
      <p class="identity__title">Job Title</p>
    </div>
    <ul class="contacts">
      <li class="contacts__item">
        <svg class="contacts__icon" viewBox="0 0 16 16" aria-hidden="true"><path d="M3 1h3l1 4-2 1c1 2 2 3 4 4l1-2 4 1v3c0 1-1 2-2 2C6 14 2 10 2 3c0-1 0-2 1-2z"/></svg>
        000 000 0000
      </li>
      <li class="contacts__item">
        <svg class="contacts__icon" viewBox="0 0 16 16" aria-hidden="true"><circle cx="8" cy="8" r="7"/><circle cx="8" cy="8" r="3" fill="#eceeed"/></svg>
        youremail@korveltait.example
      </li>
      <li class="contacts__item">
        <svg class="contacts__icon" viewBox="0 0 16 16" aria-hidden="true"><rect x="1" y="2" width="14" height="9" rx="1"/><rect x="5" y="12" width="6" height="2"/></svg>
        www.korveltait.example
      </li>
    </ul>
    <div class="brand brand--front">
      <span class="brand__mark"></span>
      <span class="brand__name">KORVELTA</span>
    </div>
  </section>

  <section class="card card--back">
    <div class="brand brand--back">
      <span class="brand__mark"></span>
      <span class="brand__name">KORVELTA</span>
    </div>
  </section>
</main>
</body>
</html>
```